CoverLantern.com website re-design - modern engaging website creation

We have an existing website. Www.CoverLantern.com - the content on the site and our widgets are custom built. But the layout and design of our site we just put there as we built the functionality around it. We want a new, bold, and modern design aimed at getting visitors to run a life insurance quote and ultimately apply. Our demographic is centered around those between the ages of 30-60. So we are looking at a complete site overhaul with better pictures, buttons, and an extremely modern design.

Target Market(s)

30-50 year olds

Industry/Entity Type

Life insurance

Coding

Coded - Design and coding required

Number of Pages Required

5+ page

Font styles to use
Other font styles liked:
• Rubik

Colors
0054AA
0677BA
7BADD7
CADEEF
E8F1F8
00AB8E
00BBA5
67D7C9
C6EFE9
E9F9F6
59FF00
82FF00
B8FF75
E3FFCB
F4FFEA

Requirements
Must have
• Matching color schemes from existing website. We have custom widgets on our site now and those must be . White space is important to make it simple for the user to navigate
Nice to have
• Same content - different more modern design
Should not have
• Colors outside of our current color scheme. Should NOT be too similar to our existing site.

```html
<!DOCTYPE html>
<html lang="en">
<head>
<meta charset="utf-8">
<title>CoverLantern – Free Quote Flow</title>
<link href="https://fonts.googleapis.com/css2?family=Rubik:wght@300;400;500;600;700&display=swap" rel="stylesheet">
<style>
:root{
  --blue:#0054AA;
  --blue-mid:#0677BA;
  --blue-soft:#7BADD7;
  --blue-pale:#CADEEF;
  --blue-wash:#E8F1F8;
  --card:#EEF4FA;
  --teal:#00AB8E;
  --lime:#8BD45A;
  --lime-band:#F4F7EE;
  --ink:#1C1C1C;
  --muted:#8A8F96;
  --line:#D6D9DD;
  --footer:#EFEFF0;
}
*{box-sizing:border-box;margin:0;padding:0}
html,body{width:1200px;height:4938px;overflow:hidden;background:#fff;font-family:'Rubik',sans-serif;color:var(--ink)}
.screen{position:relative;width:1200px;background:#fff}
.frame{position:absolute;left:0;right:0;top:0}
.brand{position:absolute;font-size:34px;font-weight:400;color:var(--blue-mid);letter-spacing:-.5px}
.site-head .brand{left:165px;top:62px}
.head-actions{position:absolute;right:155px;top:64px;display:flex;gap:10px}
.pill{height:26px;padding:0 12px;border-radius:4px;font-size:8px;font-weight:700;letter-spacing:.4px;color:#fff;display:flex;align-items:center;text-transform:uppercase}
.pill.green{background:var(--lime)}
.pill.blue{background:var(--blue)}
.site-nav{position:absolute;right:155px;top:108px;display:flex;gap:22px;font-size:9px;font-weight:500;color:#666;text-transform:uppercase}
.progress{position:absolute;left:159px;right:155px;top:170px;height:22px}
.back{position:absolute;display:flex;align-items:center;gap:12px;font-size:19px;color:var(--ink)}
.back svg{width:14px;height:20px}
.back.faded{color:var(--muted)}
.progress .back{left:0;top:0}
.bar{position:absolute;top:8px;height:7px;width:190px;border-radius:4px;background:var(--blue-wash)}
.bar.on{background:var(--blue-mid)}
.bar.b1{left:130px}.bar.b2{left:345px}.bar.b3{left:560px}
.step-label{position:absolute;right:0;top:1px;font-size:16px;font-weight:600}
.title{position:absolute;font-size:32px;font-weight:500}
.label{position:absolute;font-size:19px;line-height:1.3}
.option{position:absolute;display:flex;align-items:center;gap:18px;font-size:19px}
.radio{width:15px;height:15px;border:2px solid var(--blue-mid);border-radius:50%;position:relative;flex:none}
.radio.checked::after{content:"";position:absolute;inset:2px;border-radius:50%;background:var(--blue-mid)}
.field{position:absolute;height:44px;border:1.5px solid var(--line);border-radius:5px;display:flex;align-items:center;justify-content:space-between;padding:0 14px 0 22px;font-size:19px;color:#A6ABB1;letter-spacing:.5px}
.field svg{width:18px;height:18px;fill:#A6ABB1}
.btn{position:absolute;height:58px;border-radius:5px;background:var(--blue);color:#fff;font-size:21px;font-weight:500;display:flex;align-items:center;justify-content:center;letter-spacing:.5px}
.btn.lime{background:var(--lime);font-size:25px}
.info-card{position:absolute;background:var(--card);padding:30px 26px;color:#333}
.info-card h4{font-size:11.5px;font-weight:600;margin-bottom:18px}
.info-card .group{font-size:11px;margin:16px 0 6px}
.info-card ul{list-style:none}
.info-card li{position:relative;padding-left:18px;font-size:10.5px;line-height:1.9}
.info-card li::before{content:"";position:absolute;left:0;top:5px;width:9px;height:9px;border-radius:50%;background:var(--blue-mid)}
.info-card li.soft::before{background:var(--blue-soft)}
.info-card a{color:var(--blue-mid);text-decoration:none}
.illustration{position:absolute;border-radius:50% 50% 40% 40%;background:radial-gradient(circle at 60% 50%,#cfe0f2 0%,#e8f1f8 60%,#fff 100%)}

.site-foot{position:absolute;left:0;width:1200px;height:248px;background:var(--footer)}
.site-foot .brand{left:32px;top:36px;font-size:36px}
.foot-addr{position:absolute;left:32px;top:116px;display:flex;gap:10px;font-size:12px;line-height:1.6;color:#333;text-transform:uppercase}
.foot-addr svg{width:20px;height:16px;margin-top:4px;flex:none}
.foot-social{position:absolute;left:38px;top:184px;display:flex;gap:18px}
.foot-social span{width:22px;height:22px;border-radius:50%;background:var(--blue)}
.foot-col{position:absolute;top:24px}
.foot-col h5{font-size:14px;font-weight:500;margin-bottom:24px}
.foot-col li{list-style:none;font-size:12px;color:#444;line-height:30.5px;padding-left:4px}
.contact-line{display:flex;gap:10px;font-size:12px;color:#444;margin-bottom:22px;line-height:1.5}
.contact-line svg{width:16px;height:16px;flex:none;margin-top:1px}

.result-band{position:absolute;left:117px;width:966px;height:109px;background:var(--lime-band)}
.result-band .back{left:42px;top:42px}
.result-band h2{position:absolute;left:0;right:0;top:36px;text-align:center;font-size:33px;font-weight:500}
.term{position:absolute;left:0;right:0;text-align:center;font-size:32px;font-weight:500}
.col-head{position:absolute;font-size:26px}
.quote-row{position:absolute;left:117px;width:966px;height:121px}
.quote-row.best{border:3px solid var(--blue)}
.carrier{position:absolute;left:42px;top:50%;transform:translateY(-50%);font-size:30px;font-weight:500;color:var(--blue);display:flex;align-items:center;gap:10px}
.carrier i{width:26px;height:26px;border-radius:50%;background:var(--blue-mid);display:block}
.help{position:absolute;left:322px;top:50%;transform:translateY(-50%);width:22px;height:22px;border:1.5px solid #444;border-radius:50%;font-size:13px;display:flex;align-items:center;justify-content:center}
.price{position:absolute;left:440px;top:50%;transform:translateY(-50%);display:flex;align-items:flex-start;gap:4px}
.price b{font-size:52px;font-weight:600;line-height:1}
.price small{font-size:16px;line-height:1.2;margin-top:8px}
.best-tag{position:absolute;left:620px;top:50%;transform:translateY(-50%);display:flex;align-items:center;gap:8px;font-size:14px;color:#444}
.apply{position:absolute;left:763px;top:50%;transform:translateY(-50%);width:160px;height:36px;border-radius:4px;background:var(--blue);color:#fff;font-size:21px;font-weight:600;display:flex;align-items:center;justify-content:center}
</style>
</head>
<body>

<!-- Step 1 -->
<section class="screen" style="height:757px">
  <div class="frame">
    <header class="site-head">
      <div class="brand">CoverLantern</div>
      <div class="head-actions"><span class="pill green">Continue Application</span><span class="pill blue">Existing Client Login</span></div>
      <nav class="site-nav"><span>Free Quote</span><span>No Exam</span><span>Articles</span><span>FAQ's</span><span>About</span><span>Contact</span></nav>
    </header>
    <div class="progress">
      <div class="back faded"><svg viewBox="0 0 14 20"><path d="M11 2 3 10l8 8" fill="none" stroke="currentColor" stroke-width="2.5"/></svg>Back</div>
      <div class="bar b1 on"></div><div class="bar b2"></div><div class="bar b3"></div>
      <div class="step-label">Step 1 - 3</div>
    </div>
    <h1 class="title" style="left:159px;top:238px">Free Quote</h1>
    <div style="position:absolute;left:159px;top:338px">
      <div style="font-size:14px;font-weight:600">What State do you live in?</div>
      <div style="font-size:11px;color:var(--muted);margin-top:8px">Pick Your State</div>
    </div>
    <div class="field" style="left:406px;top:333px;width:290px">California<svg viewBox="0 0 24 24"><path d="M12 2a7 7 0 0 0-7 7c0 5 7 13 7 13s7-8 7-13a7 7 0 0 0-7-7zm0 9.5A2.5 2.5 0 1 1 12 6.5a2.5 2.5 0 0 1 0 5z"/></svg></div>
    <div class="btn" style="left:159px;top:423px;width:537px">Next</div>
    <div class="illustration" role="img" aria-label="Illustration of a family standing together under a protective shield" style="left:790px;top:230px;width:215px;height:160px"></div>
    <aside class="info-card" style="left:767px;top:406px;width:278px;height:309px;border-radius:24px">
      <h4>What State do you live in?</h4>
      <ul>
        <li class="soft">Free Online Term Quotes</li>
        <li class="soft">Compare America's top rated carriers.</li>
        <li class="soft">No Sales Agent</li>
        <li class="soft">No contact information is required unless you decide to apply for coverage</li>
        <li class="soft">Safe &amp; Secure Online Application process.</li>
      </ul>
    </aside>
  </div>
</section>

<footer class="site-foot" style="top:757px">
  <div class="brand">CoverLantern</div>
  <div class="foot-addr"><svg viewBox="0 0 20 16"><rect x="1" y="1" width="18" height="14" rx="2" fill="none" stroke="#7BAA3A" stroke-width="1.6"/><circle cx="7" cy="7" r="2" fill="#7BAA3A"/><path d="M12 6h5M12 9h5M4 12h7" stroke="#7BAA3A" stroke-width="1.4"/></svg><span>4120 Lakeshore Avenue, Suite 310<br>Brookhaven, FL 34990</span></div>
  <div class="foot-social"><span></span><span></span><span></span><span></span></div>
  <div class="foot-col" style="left:380px"><h5>Life Insurance Products</h5><ul><li>10 Year Level Team</li><li>15 Year Level Team</li><li>20 Year Level Team</li><li>30 Year Level Team</li><li>Lifetime Coverage</li></ul></div>
  <div class="foot-col" style="left:610px"><h5>Tools</h5><ul><li>Quote Comparison</li><li>Secure Client Portal</li><li>Privacy Policy</li></ul></div>
  <div class="foot-col" style="left:840px"><h5>Social</h5><ul><li>Newsletter</li><li>Updates</li><li>Gallery</li><li>Community</li><li>Careers</li></ul></div>
  <div class="foot-col" style="left:953px"><h5>Contact</h5>
    <div class="contact-line"><svg viewBox="0 0 16 16"><rect x="1" y="3" width="14" height="10" rx="1" fill="none" stroke="#7BAA3A" stroke-width="1.5"/><path d="m1.5 3.5 6.5 5 6.5-5" fill="none" stroke="#7BAA3A" stroke-width="1.5"/></svg>info@CoverLantern.com</div>
    <div class="contact-line"><svg viewBox="0 0 16 16"><path d="M4 1.5 6 5 4.5 6.5a9 9 0 0 0 5 5L11 10l3.5 2-1 2.5C7 14.5 1.5 9 1.5 2.5z" fill="none" stroke="#7BAA3A" stroke-width="1.5"/></svg>1-888-555-0142</div>
    <div class="contact-line"><svg viewBox="0 0 16 16"><circle cx="8" cy="8" r="6.5" fill="none" stroke="#7BAA3A" stroke-width="1.5"/><path d="M8 4v4l3 2" fill="none" stroke="#7BAA3A" stroke-width="1.5"/></svg><span>Monday - Friday<br>9:00 AM - 8:00 PM</span></div>
  </div>
</footer>

<!-- Step 2 -->
<section class="screen" style="position:absolute;top:1005px;height:1021px">
  <div class="frame" style="top:30px">
    <header class="site-head">
      <div class="brand">CoverLantern</div>
      <div class="head-actions"><span class="pill green">Continue Application</span><span class="pill blue">Existing Client Login</span></div>
      <nav class="site-nav"><span>Free Quote</span><span>No Exam</span><span>Articles</span><span>FAQ's</span><span>About</span><span>Contact</span></nav>
    </header>
    <div class="progress">
      <div class="back"><svg viewBox="0 0 14 20"><path d="M11 2 3 10l8 8" fill="none" stroke="var(--blue-mid)" stroke-width="2.5"/></svg>Back</div>
      <div class="bar b1 on"></div><div class="bar b2 on"></div><div class="bar b3"></div>
      <div class="step-label">Step 2 - 3</div>
    </div>
    <h1 class="title" style="left:153px;top:248px">Please provide some health background</h1>
    <div class="label" style="left:153px;top:343px">Sex</div>
    <div class="option" style="left:456px;top:345px"><span class="radio checked"></span>Male</div>
    <div class="option" style="left:588px;top:345px"><span class="radio"></span>Female</div>
    <div class="label" style="left:153px;top:440px">Your Date of Birth</div>
    <div class="field" style="left:455px;top:430px;width:241px">MM/DD/YYYY<svg viewBox="0 0 24 24"><path d="M4 5h16v16H4zM4 9h16M8 3v4M16 3v4" fill="none" stroke="#A6ABB1" stroke-width="2"/></svg></div>
    <div class="label" style="left:153px;top:535px">Please rate your health.</div>
    <div class="option" style="left:456px;top:535px"><span class="radio"></span>Excellent</div>
    <div class="option" style="left:456px;top:583px"><span class="radio checked"></span>Good</div>
    <div class="option" style="left:456px;top:631px"><span class="radio"></span>Ok</div>
    <div class="label" style="left:153px;top:692px">Do you use any tobacco or<br>nicotine products?</div>
    <div class="option" style="left:456px;top:704px"><span class="radio checked"></span>Yes</div>
    <div class="option" style="left:632px;top:704px"><span class="radio"></span>No</div>
    <div class="btn" style="left:153px;top:801px;width:543px">Next</div>
    <aside class="info-card" style="left:767px;top:341px;width:274px;height:506px;padding-top:70px">
      <h4>How to rate your health</h4>
      <div class="group">Excellent</div>
      <ul><li>Healthy Weight/BMI</li><li>No Medical Conditions</li><li>No Medications</li></ul>
      <div class="group">Good</div>
      <ul><li>Normal Weight</li><li>Minor pre-existing Medical Conditions</li><li>Controlled minor medical conditions (HBP/Cholesterol)</li></ul>
      <div class="group">Good</div>
      <ul><li>Overweight</li><li>Diabetes</li><li>Uncontrolled HBP/Cholesterol</li></ul>
    </aside>
  </div>
</section>

<footer class="site-foot" style="top:2026px">
  <div class="brand">CoverLantern</div>
  <div class="foot-addr"><svg viewBox="0 0 20 16"><rect x="1" y="1" width="18" height="14" rx="2" fill="none" stroke="#7BAA3A" stroke-width="1.6"/><circle cx="7" cy="7" r="2" fill="#7BAA3A"/><path d="M12 6h5M12 9h5M4 12h7" stroke="#7BAA3A" stroke-width="1.4"/></svg><span>4120 Lakeshore Avenue, Suite 310<br>Brookhaven, FL 34990</span></div>
  <div class="foot-social"><span></span><span></span><span></span><span></span></div>
  <div class="foot-col" style="left:380px"><h5>Life Insurance Products</h5><ul><li>10 Year Level Team</li><li>15 Year Level Team</li><li>20 Year Level Team</li><li>30 Year Level Team</li><li>Lifetime Coverage</li></ul></div>
  <div class="foot-col" style="left:610px"><h5>Tools</h5><ul><li>Quote Comparison</li><li>Secure Client Portal</li><li>Privacy Policy</li></ul></div>
  <div class="foot-col" style="left:840px"><h5>Social</h5><ul><li>Newsletter</li><li>Updates</li><li>Gallery</li><li>Community</li><li>Careers</li></ul></div>
  <div class="foot-col" style="left:953px"><h5>Contact</h5>
    <div class="contact-line"><svg viewBox="0 0 16 16"><rect x="1" y="3" width="14" height="10" rx="1" fill="none" stroke="#7BAA3A" stroke-width="1.5"/><path d="m1.5 3.5 6.5 5 6.5-5" fill="none" stroke="#7BAA3A" stroke-width="1.5"/></svg>info@CoverLantern.com</div>
    <div class="contact-line"><svg viewBox="0 0 16 16"><path d="M4 1.5 6 5 4.5 6.5a9 9 0 0 0 5 5L11 10l3.5 2-1 2.5C7 14.5 1.5 9 1.5 2.5z" fill="none" stroke="#7BAA3A" stroke-width="1.5"/></svg>1-888-555-0142</div>
    <div class="contact-line"><svg viewBox="0 0 16 16"><circle cx="8" cy="8" r="6.5" fill="none" stroke="#7BAA3A" stroke-width="1.5"/><path d="M8 4v4l3 2" fill="none" stroke="#7BAA3A" stroke-width="1.5"/></svg><span>Monday - Friday<br>9:00 AM - 8:00 PM</span></div>
  </div>
</footer>

<!-- Step 3 -->
<section class="screen" style="position:absolute;top:2274px;height:985px">
  <div class="frame" style="top:23px">
    <header class="site-head">
      <div class="brand">CoverLantern</div>
      <div class="head-actions"><span class="pill green">Continue Application</span><span class="pill blue">Existing Client Login</span></div>
      <nav class="site-nav"><span>Free Quote</span><span>No Exam</span><span>Articles</span><span>FAQ's</span><span>About</span><span>Contact</span></nav>
    </header>
    <div class="progress">
      <div class="back"><svg viewBox="0 0 14 20"><path d="M11 2 3 10l8 8" fill="none" stroke="var(--blue-mid)" stroke-width="2.5"/></svg>Back</div>
      <div class="bar b1 on"></div><div class="bar b2 on"></div><div class="bar b3 on"></div>
      <div class="step-label">Step 3 - 3</div>
    </div>
    <h1 class="title" style="left:159px;top:272px">Choose your coverage.</h1>
    <div class="label" style="left:159px;top:350px">How long do you<br>want the coverage for?</div>
    <div class="option" style="left:456px;top:350px"><span class="radio checked"></span>10 Years</div>
    <div class="option" style="left:456px;top:398px"><span class="radio"></span>15 Years</div>
    <div class="option" style="left:456px;top:446px"><span class="radio"></span>20 Years</div>
    <div class="option" style="left:456px;top:494px"><span class="radio"></span>30 Years</div>
    <div class="label" style="left:153px;top:553px">How much Death<br>Benefit would you like<br>to see quoted?</div>
    <div class="field" style="left:455px;top:558px;width:241px;font-size:13px;height:42px">$100,000 - $10,000,000<svg viewBox="0 0 24 24"><rect x="3" y="6" width="18" height="12" rx="1" fill="none" stroke="#A6ABB1" stroke-width="2"/><circle cx="12" cy="12" r="3" fill="#A6ABB1"/></svg></div>
    <div class="btn" style="left:153px;top:675px;width:543px">Compare Quotes</div>
    <aside class="info-card" style="left:767px;top:291px;width:278px;height:441px;padding-top:80px">
      <h4>How to choose your coverage.</h4>
      <ul><li>Pick a Death Benefit that will cover your debt and provide your family with an income to sustain their standard of living.</li><li>Pick a term length that will cover you during your income replacement years.</li></ul>
      <div class="group" style="margin-top:30px;font-weight:600">Unsure</div>
      <ul><li>Use our Life Insurance Calculator by <a>clicking here.</a></li></ul>
    </aside>
  </div>
</section>

<footer class="site-foot" style="top:3259px">
  <div class="brand">CoverLantern</div>
  <div class="foot-addr"><svg viewBox="0 0 20 16"><rect x="1" y="1" width="18" height="14" rx="2" fill="none" stroke="#7BAA3A" stroke-width="1.6"/><circle cx="7" cy="7" r="2" fill="#7BAA3A"/><path d="M12 6h5M12 9h5M4 12h7" stroke="#7BAA3A" stroke-width="1.4"/></svg><span>4120 Lakeshore Avenue, Suite 310<br>Brookhaven, FL 34990</span></div>
  <div class="foot-social"><span></span><span></span><span></span><span></span></div>
  <div class="foot-col" style="left:380px"><h5>Life Insurance Products</h5><ul><li>10 Year Level Team</li><li>15 Year Level Team</li><li>20 Year Level Team</li><li>30 Year Level Team</li><li>Lifetime Coverage</li></ul></div>
  <div class="foot-col" style="left:610px"><h5>Tools</h5><ul><li>Quote Comparison</li><li>Secure Client Portal</li><li>Privacy Policy</li></ul></div>
  <div class="foot-col" style="left:840px"><h5>Social</h5><ul><li>Newsletter</li><li>Updates</li><li>Gallery</li><li>Community</li><li>Careers</li></ul></div>
  <div class="foot-col" style="left:953px"><h5>Contact</h5>
    <div class="contact-line"><svg viewBox="0 0 16 16"><rect x="1" y="3" width="14" height="10" rx="1" fill="none" stroke="#7BAA3A" stroke-width="1.5"/><path d="m1.5 3.5 6.5 5 6.5-5" fill="none" stroke="#7BAA3A" stroke-width="1.5"/></svg>info@CoverLantern.com</div>
    <div class="contact-line"><svg viewBox="0 0 16 16"><path d="M4 1.5 6 5 4.5 6.5a9 9 0 0 0 5 5L11 10l3.5 2-1 2.5C7 14.5 1.5 9 1.5 2.5z" fill="none" stroke="#7BAA3A" stroke-width="1.5"/></svg>1-888-555-0142</div>
    <div class="contact-line"><svg viewBox="0 0 16 16"><circle cx="8" cy="8" r="6.5" fill="none" stroke="#7BAA3A" stroke-width="1.5"/><path d="M8 4v4l3 2" fill="none" stroke="#7BAA3A" stroke-width="1.5"/></svg><span>Monday - Friday<br>9:00 AM - 8:00 PM</span></div>
  </div>
</footer>

<!-- Compare quotes -->
<section class="screen" style="position:absolute;top:3507px;height:1183px">
  <div class="frame" style="top:22px">
    <header class="site-head">
      <div class="brand">CoverLantern</div>
      <div class="head-actions"><span class="pill green">Continue Application</span><span class="pill blue">Existing Client Login</span></div>
      <nav class="site-nav"><span>Free Quote</span><span>No Exam</span><span>Articles</span><span>FAQ's</span><span>About</span><span>Contact</span></nav>
    </header>
    <div class="result-band" style="top:138px">
      <div class="back"><svg viewBox="0 0 14 20"><path d="M11 2 3 10l8 8" fill="none" stroke="var(--blue-mid)" stroke-width="2.5"/></svg>Back</div>
      <h2>Compare Quotes</h2>
    </div>
    <div class="term" style="top:292px">$1,000,000 20 Year Term</div>
    <div class="col-head" style="left:528px;top:389px">Monthly cost</div>
    <div class="col-head" style="left:879px;top:389px">Pick your policy</div>

    <div class="quote-row best" style="top:464px">
      <div class="carrier">Harlow Mutual</div>
      <div class="help">?</div>
      <div class="price"><b>$54</b><small>91<br>/MO</small></div>
      <div class="best-tag"><svg width="16" height="16" viewBox="0 0 24 24"><path d="m12 2 3 7 7 .5-5.5 4.5 2 7.5L12 17l-6.5 4.5 2-7.5L2 9.5 9 9z" fill="#F5A623"/></svg>Best Value</div>
      <div class="apply">Apply Now</div>
    </div>
    <div class="quote-row" style="top:589px">
      <div class="carrier">Steadfast Life <i></i></div>
      <div class="help">?</div>
      <div class="price"><b>$59</b><small>60<br>/MO</small></div>
      <div class="apply">Apply Now</div>
    </div>
    <div class="quote-row" style="top:717px">
      <div class="carrier"><i></i> Keystone Financial</div>
      <div class="help">?</div>
      <div class="price"><b>$63</b><small>11<br>/MO</small></div>
      <div class="apply">Apply Now</div>
    </div>
    <div class="quote-row" style="top:838px">
      <div class="carrier">Meridian Life</div>
      <div class="help">?</div>
      <div class="price"><b>$72</b><small>52<br>/MO</small></div>
      <div class="apply">Apply Now</div>
    </div>

    <div class="back" style="left:159px;top:1028px"><svg viewBox="0 0 14 20"><path d="M11 2 3 10l8 8" fill="none" stroke="var(--blue-mid)" stroke-width="2.5"/></svg>Back</div>
    <div class="btn lime" style="left:772px;top:1010px;width:311px">Save/Email Quote</div>
  </div>
</section>

<footer class="site-foot" style="top:4690px">
  <div class="brand">CoverLantern</div>
  <div class="foot-addr"><svg viewBox="0 0 20 16"><rect x="1" y="1" width="18" height="14" rx="2" fill="none" stroke="#7BAA3A" stroke-width="1.6"/><circle cx="7" cy="7" r="2" fill="#7BAA3A"/><path d="M12 6h5M12 9h5M4 12h7" stroke="#7BAA3A" stroke-width="1.4"/></svg><span>4120 Lakeshore Avenue, Suite 310<br>Brookhaven, FL 34990</span></div>
  <div class="foot-social"><span></span><span></span><span></span><span></span></div>
  <div class="foot-col" style="left:380px"><h5>Life Insurance Products</h5><ul><li>10 Year Level Team</li><li>15 Year Level Team</li><li>20 Year Level Team</li><li>30 Year Level Team</li><li>Lifetime Coverage</li></ul></div>
  <div class="foot-col" style="left:610px"><h5>Tools</h5><ul><li>Quote Comparison</li><li>Secure Client Portal</li><li>Privacy Policy</li></ul></div>
  <div class="foot-col" style="left:840px"><h5>Social</h5><ul><li>Newsletter</li><li>Updates</li><li>Gallery</li><li>Community</li><li>Careers</li></ul></div>
  <div class="foot-col" style="left:953px"><h5>Contact</h5>
    <div class="contact-line"><svg viewBox="0 0 16 16"><rect x="1" y="3" width="14" height="10" rx="1" fill="none" stroke="#7BAA3A" stroke-width="1.5"/><path d="m1.5 3.5 6.5 5 6.5-5" fill="none" stroke="#7BAA3A" stroke-width="1.5"/></svg>info@CoverLantern.com</div>
    <div class="contact-line"><svg viewBox="0 0 16 16"><path d="M4 1.5 6 5 4.5 6.5a9 9 0 0 0 5 5L11 10l3.5 2-1 2.5C7 14.5 1.5 9 1.5 2.5z" fill="none" stroke="#7BAA3A" stroke-width="1.5"/></svg>1-888-555-0142</div>
    <div class="contact-line"><svg viewBox="0 0 16 16"><circle cx="8" cy="8" r="6.5" fill="none" stroke="#7BAA3A" stroke-width="1.5"/><path d="M8 4v4l3 2" fill="none" stroke="#7BAA3A" stroke-width="1.5"/></svg><span>Monday - Friday<br>9:00 AM - 8:00 PM</span></div>
  </div>
</footer>

</body>
</html>
```